COVID-19 Site Safety Signage

Creation of a COVID-19 Health and Safety Sign for a building site. 600mm WIDE. 800mm HIGH. The information would be shown as icons as per the attached references. You CANNOT copy the references exactly as they belong to another business. The sign would also include a QR code and instructions at the bottom (as per one of the references). Note: I am waiting on supply of the QR code. Please use a placeholder for now.

The QUELBRAM COVID BOARD reference closely matches our branding (colours, text, minimalist icons).

Please make allowance to supply .ai file format and all associated artwork.

Please ensure the icons/text you use are original or free to use commercially.

Target Market(s)

Builders, tradesmen

Font styles to use
Sans Serif

Colors

Designer to choose only greyscale colors for use in the design.

Requirements
Must have
• Black background. White text and icons.

QR code with room for instructions.

Supply .ai files.
Nice to have
Should not have

```html
<!DOCTYPE html>
<html lang="en">
<head>
<meta charset="utf-8">
<title>COVID-19 Behavioural Controls &amp; Hygiene Sign</title>
<link href="https://fonts.googleapis.com/css2?family=Montserrat:wght@900&family=Oswald:wght@300;400;500&family=Open+Sans:wght@600;700&display=swap" rel="stylesheet">
<style>
  :root {
    --black: #111111;
    --white: #ffffff;
    --grey-light: #c8c8c8;
    --grey-mid: #8a8a8a;
    --grey-dark: #333333;
    --stripe: #d6d6d6;
    --backdrop: #e4e4e2;
  }
  * { box-sizing: border-box; margin: 0; padding: 0; }
  html, body { width: 1200px; height: 960px; overflow: hidden; }
  body { background: var(--backdrop); position: relative; }

  .sign {
    position: absolute; left: 254px; top: 20px; width: 692px; height: 920px;
    background: repeating-linear-gradient(45deg, var(--black) 0 14px, var(--stripe) 14px 30px);
    box-shadow: 0 6px 20px rgba(0,0,0,.25);
  }
  .sign__panel { position: absolute; inset: 20px; background: var(--black); }
  .sign__body { position: absolute; left: 0; top: 0; width: 692px; height: 920px; color: var(--white); }

  .abs { position: absolute; }

  .title {
    left: 0; width: 692px; top: 44px; text-align: center;
    font-family: 'Montserrat', sans-serif; font-weight: 900; font-size: 84px;
    color: var(--white); letter-spacing: -3px; line-height: 1;
  }
  .banner {
    left: 44px; top: 130px; width: 604px; height: 56px; background: var(--white);
    border-radius: 3px; display: flex; align-items: center; justify-content: center;
    font-family: 'Oswald', sans-serif; font-weight: 500; font-size: 40px;
    color: var(--black); letter-spacing: 0.5px;
  }

  .section-head {
    font-family: 'Oswald', sans-serif; font-weight: 400; font-size: 25px;
    line-height: 29px; color: var(--white); padding-left: 12px;
    border-left: 3px solid var(--grey-light);
  }
  .section-intro {
    font-family: 'Oswald', sans-serif; font-weight: 300; font-size: 14.5px;
    line-height: 18px; color: var(--grey-light);
  }
  .rule { height: 1.5px; background: var(--grey-mid); }
  .sub-head {
    font-family: 'Open Sans', sans-serif; font-weight: 600; font-size: 16.5px;
    color: var(--white);
  }

  .item { display: flex; align-items: flex-start; gap: 12px; }
  .item__icon { width: 34px; height: 32px; flex: none; }
  .item__text {
    font-family: 'Open Sans', sans-serif; font-weight: 600; font-size: 10.5px;
    line-height: 14px; color: var(--white); white-space: nowrap;
  }
  .item--split { gap: 10px; }
  .item--split .item__text { border-left: 1px solid var(--grey-mid); padding-left: 7px; margin-left: -3px; }

  .footer-rule { left: 46px; top: 834px; width: 600px; height: 1.5px; background: var(--grey-mid); }
  .qr-placeholder {
    left: 46px; top: 843px; width: 52px; height: 52px;
    border: 2px dashed var(--grey-light); background: var(--grey-dark);
  }
  .qr-instructions { left: 110px; top: 846px; width: 260px; }
  .qr-instructions__head {
    font-family: 'Open Sans', sans-serif; font-weight: 700; font-size: 12px;
    color: var(--white); letter-spacing: .3px;
  }
  .qr-instructions__text {
    font-family: 'Open Sans', sans-serif; font-weight: 600; font-size: 10.5px;
    line-height: 14px; color: var(--grey-light); margin-top: 3px;
  }
  .footer-label {
    right: 46px; font-family: 'Open Sans', sans-serif; font-weight: 700; font-size: 12px;
    color: var(--white); letter-spacing: .3px; text-align: right;
  }
</style>
</head>
<body>
<svg width="0" height="0" style="position:absolute" aria-hidden="true">
  <defs>
    <symbol id="tick" viewBox="0 0 10 10"><path d="M1 5.5 L4 8.5 L9 1.5" fill="none" stroke="#ffffff" stroke-width="2" stroke-linecap="round" stroke-linejoin="round"/></symbol>
    <symbol id="i-house" viewBox="0 0 34 32"><path d="M4 15 L16 4 L28 15 H25 V28 H7 V15 Z" fill="#fff"/><use href="#tick" x="22" y="20" width="11" height="11"/></symbol>
    <symbol id="i-phone" viewBox="0 0 34 32"><path d="M6 5 C4 6 3 9 5 13 C8 20 13 25 20 27 C23 28 25 26 26 24 L21 19 L18 21 C15 19 13 17 11 14 L13 11 Z" fill="#fff"/><rect x="18" y="3" width="10" height="10" rx="1" fill="#fff"/><rect x="22.3" y="5" width="1.6" height="4.5" fill="#111"/><use href="#tick" x="22" y="20" width="11" height="11"/></symbol>
    <symbol id="i-clock" viewBox="0 0 34 32"><circle cx="15" cy="15" r="12" fill="#fff"/><path d="M15 7 V15 H21" fill="none" stroke="#111" stroke-width="2"/><use href="#tick" x="22" y="20" width="11" height="11"/></symbol>
    <symbol id="i-bin" viewBox="0 0 34 32"><rect x="7" y="8" width="16" height="3" fill="#fff"/><rect x="13" y="4" width="4" height="4" fill="#fff"/><path d="M9 12 H21 L20 28 H10 Z" fill="#fff"/><path d="M12.5 14 V26 M15 14 V26 M17.5 14 V26" stroke="#111" stroke-width="1"/><use href="#tick" x="22" y="20" width="11" height="11"/></symbol>
    <symbol id="i-bottle" viewBox="0 0 34 32"><rect x="12" y="2" width="6" height="4" fill="#fff"/><rect x="9" y="8" width="12" height="20" rx="2" fill="#fff"/><path d="M15 13 V21 M11 17 H19" stroke="#111" stroke-width="2"/><use href="#tick" x="22" y="20" width="11" height="11"/></symbol>
    <symbol id="i-dot" viewBox="0 0 34 32"><circle cx="15" cy="15" r="12" fill="#fff"/><circle cx="15" cy="15" r="5" fill="#111"/><use href="#tick" x="22" y="20" width="11" height="11"/></symbol>
    <symbol id="i-block" viewBox="0 0 34 32"><rect x="3" y="6" width="24" height="19" rx="3" fill="#fff"/><rect x="8" y="12" width="14" height="3" fill="#111"/><use href="#tick" x="22" y="20" width="11" height="11"/></symbol>
    <symbol id="i-cross" viewBox="0 0 34 32"><rect x="5" y="6" width="20" height="20" rx="4" fill="#fff"/><path d="M15 10 V22 M9 16 H21" stroke="#111" stroke-width="3"/><use href="#tick" x="22" y="20" width="11" height="11"/></symbol>
    <symbol id="i-14" viewBox="0 0 34 32"><circle cx="15" cy="15" r="13" fill="#fff"/><text x="15" y="19" text-anchor="middle" font-family="Open Sans, sans-serif" font-weight="700" font-size="12" fill="#111">14</text><use href="#tick" x="22" y="20" width="11" height="11"/></symbol>
  </defs>
</svg>

<main class="sign">
  <div class="sign__panel"></div>
  <div class="sign__body">
    <h1 class="abs title">COVID-19</h1>
    <div class="abs banner">BEHAVIOURAL CONTROLS &amp; HYGIENE</div>

    <!-- Simple steps -->
    <h2 class="abs section-head" style="left:46px;top:212px">SIMPLE STEPS TO STOP<br>THE SPREAD</h2>
    <p class="abs section-intro" style="left:59px;top:282px">There are some simple steps in the workplace<br>to help stop the spread of COVID-19.</p>
    <div class="abs rule" style="left:59px;top:329px;width:284px"></div>

    <div class="abs item" style="left:57px;top:349px"><svg class="item__icon"><use href="#i-dot"/></svg><p class="item__text">Screen for risks of<br>potential exposure<br>before entering site</p></div>
    <div class="abs item" style="left:214px;top:349px"><svg class="item__icon"><use href="#i-house"/></svg><p class="item__text">Stay at home if<br>you feel sick</p></div>
    <div class="abs item" style="left:57px;top:409px"><svg class="item__icon"><use href="#i-dot"/></svg><p class="item__text">Wash hands<br>regularly</p></div>
    <div class="abs item" style="left:214px;top:398px"><svg class="item__icon"><use href="#i-bottle"/></svg><p class="item__text">Use hand sanitiser<br>provided</p></div>
    <div class="abs item" style="left:57px;top:451px"><svg class="item__icon"><use href="#i-dot"/></svg><p class="item__text">Cough or sneeze<br>into your elbow</p></div>
    <div class="abs item" style="left:214px;top:447px"><svg class="item__icon"><use href="#i-bin"/></svg><p class="item__text">Place rubbish in<br>bins provided</p></div>
    <div class="abs item" style="left:57px;top:496px"><svg class="item__icon"><use href="#i-dot"/></svg><p class="item__text">Use appropriate<br>PPE</p></div>
    <div class="abs item" style="left:214px;top:494px"><svg class="item__icon"><use href="#i-dot"/></svg><p class="item__text">Don't touch<br>your face</p></div>
    <div class="abs item" style="left:57px;top:540px"><svg class="item__icon"><use href="#i-dot"/></svg><p class="item__text">Conduct regular toolbox meetings to share<br>information (observe physical distancing)</p></div>

    <!-- Maintaining shared spaces -->
    <h2 class="abs section-head" style="left:46px;top:587px">MAINTAINING SHARED<br>SPACES AND EQUIPMENT</h2>
    <p class="abs section-intro" style="left:59px;top:657px">Recommended controls minimise the risk of<br>spreading COVID-19 on work sites.</p>
    <div class="abs rule" style="left:59px;top:701px;width:284px"></div>

    <div class="abs item" style="left:57px;top:718px"><svg class="item__icon"><use href="#i-dot"/></svg><p class="item__text">Clean tools<br>before and after use</p></div>
    <div class="abs item" style="left:214px;top:718px"><svg class="item__icon"><use href="#i-dot"/></svg><p class="item__text">Clean frequently<br>touched surfaces</p></div>
    <div class="abs item" style="left:57px;top:756px"><svg class="item__icon"><use href="#i-block"/></svg><p class="item__text">Eat at designated<br>locations every day</p></div>
    <div class="abs item" style="left:214px;top:756px"><svg class="item__icon"><use href="#i-bottle"/></svg><p class="item__text">Clean plant<br>and equipment<br>after use</p></div>
    <div class="abs item" style="left:57px;top:794px"><svg class="item__icon"><use href="#i-block"/></svg><p class="item__text">Clean work<br>vehicles regularly</p></div>

    <!-- Physical distancing -->
    <h2 class="abs section-head" style="left:371px;top:212px">PHYSICAL DISTANCING</h2>
    <p class="abs section-intro" style="left:385px;top:253px">Guidelines for maintaining distancing between<br>workers to minimise the spread of COVID-19.<br>Remember to keep 1.5 metres away from<br>others as much as possible, and where safe to do so.</p>
    <div class="abs rule" style="left:385px;top:336px;width:266px"></div>

    <div class="abs item item--split" style="left:383px;top:358px"><svg class="item__icon"><use href="#i-block"/></svg><p class="item__text">Keep<br>your distance</p></div>
    <div class="abs item item--split" style="left:530px;top:358px"><svg class="item__icon"><use href="#i-clock"/></svg><p class="item__text">Stagger start<br>and finish times</p></div>
    <div class="abs item item--split" style="left:383px;top:403px"><svg class="item__icon"><use href="#i-block"/></svg><p class="item__text">Stagger<br>lunch times</p></div>

    <!-- Self-isolation -->
    <h2 class="abs section-head" style="left:371px;top:444px">SELF-ISOLATION</h2>
    <p class="abs section-intro" style="left:385px;top:484px">Advice for workers with or without symptoms<br>of infection, who are isolating themselves due<br>to potential exposure to COVID-19.</p>
    <div class="abs rule" style="left:385px;top:548px;width:266px"></div>

    <h3 class="abs sub-head" style="left:385px;top:561px">If you have symptoms</h3>
    <div class="abs item item--split" style="left:383px;top:594px"><svg class="item__icon"><use href="#i-house"/></svg><p class="item__text">Stay at home, and<br>away from others</p></div>
    <div class="abs item item--split" style="left:556px;top:594px"><svg class="item__icon"><use href="#i-phone"/></svg><p class="item__text">Notify your<br>employer</p></div>
    <div class="abs item item--split" style="left:383px;top:638px"><svg class="item__icon"><use href="#i-phone"/></svg><p class="item__text">Ring the COVID<br>Helpline 1800 555 012</p></div>
    <div class="abs item item--split" style="left:556px;top:638px"><svg class="item__icon"><use href="#i-cross"/></svg><p class="item__text">Seek medical<br>advice</p></div>
    <div class="abs item item--split" style="left:383px;top:680px"><svg class="item__icon"><use href="#i-cross"/></svg><p class="item__text">Return to work after<br>clearance from a doctor</p></div>

    <h3 class="abs sub-head" style="left:385px;top:717px">If no symptoms</h3>
    <div class="abs item item--split" style="left:383px;top:750px"><svg class="item__icon"><use href="#i-house"/></svg><p class="item__text">Stay at<br>home</p></div>
    <div class="abs item item--split" style="left:556px;top:750px"><svg class="item__icon"><use href="#i-phone"/></svg><p class="item__text">Notify your<br>employer</p></div>
    <div class="abs item item--split" style="left:383px;top:792px"><svg class="item__icon"><use href="#i-14"/></svg><p class="item__text">Return to work after 14 days<br>if no symptoms develop</p></div>

    <!-- Footer: QR sign-in and contact -->
    <div class="abs footer-rule"></div>
    <div class="abs qr-placeholder" role="img" aria-label="QR code placeholder"></div>
    <div class="abs qr-instructions">
      <p class="qr-instructions__head">SCAN TO SIGN IN ON ARRIVAL</p>
      <p class="qr-instructions__text">Open your phone camera, scan the code and<br>complete the health check before entering site.</p>
    </div>
    <p class="abs footer-label" style="top:849px">YOUR COMPANY LOGO HERE</p>
    <p class="abs footer-label" style="top:871px">CONTACT INFO HERE</p>
  </div>
</main>
</body>
</html>
```